Business Card - Professional Minimalist - Double sided

We appreciate minimalist logo/web/collateral designs that allow design to tell a story. We want to relay a professional image/approach but throwing in a splash of modern when we’re able so long as it’s not distracting. Think 75% classic corporate, 25% modern. Open to black or white design, not sure which might look the best.

Target Market(s)

Senior executives or related government affairs contacts within the agriculture, energy, and defense industries (i.e., potential clients) but located outside of Washington, DC. Most potential clients based in DC with be familiar with both of us and our shared history.

Industry/Entity Type

Consulting

Contact Information for Business Card

Name: Daniel R. Whitlock
Title: Co-Founder & Partner
Address: 418 Bramblewood Ave. SE | Suite 2716 | Washington, D.C. 20019
Phone: (202) 555-0187
Email: Daniel@HollerbyWhitlock.com

Font styles to use
Serif

Colors

Designer to choose only greyscale colors for use in the design.

Requirements
Must have
• Name: Daniel R. Whitlock
Phone: (202) 555-0187

```html
<!DOCTYPE html>
<html lang="en">
<head>
<meta charset="utf-8">
<title>Hollerby Whitlock Group – Business Card</title>
<link href="https://fonts.googleapis.com/css2?family=Tinos:wght@400;700&display=swap" rel="stylesheet">
<style>
  :root {
    --backdrop: #d9dadc;
    --charcoal: #58595b;
    --mid-grey: #a7a9ac;
    --paper: #ffffff;
    --ink: #5b5c5e;
    --rule: #8a8b8e;
  }
  * { margin: 0; padding: 0; box-sizing: border-box; }
  html, body {
    width: 1200px;
    height: 700px;
    overflow: hidden;
    background: var(--backdrop);
  }
  .stage {
    position: relative;
    width: 1200px;
    height: 700px;
    font-family: "Tinos", "Times New Roman", serif;
  }
  .card {
    position: absolute;
    top: 211px;
    width: 484px;
    height: 277px;
    background: var(--paper);
    box-shadow: 3px 4px 7px rgba(0, 0, 0, 0.35);
    overflow: hidden;
  }
  .card--front { left: 71px; }
  .card--back { left: 628px; }
  .card__shapes {
    position: absolute;
    inset: 0;
    width: 100%;
    height: 100%;
  }

  /* front */
  .brand {
    position: absolute;
    left: 0;
    right: 0;
    top: 116px;
    display: flex;
    align-items: center;
    justify-content: center;
    gap: 10px;
  }
  .brand__square {
    width: 22px;
    height: 22px;
    background: var(--charcoal);
  }
  .brand__name {
    font-size: 21px;
    font-weight: 400;
    letter-spacing: 0.5px;
    color: var(--charcoal);
    line-height: 1;
  }

  /* back */
  .person {
    position: absolute;
    left: 26px;
    top: 40px;
    color: var(--ink);
  }
  .person__name {
    font-size: 27px;
    font-weight: 700;
    line-height: 1.1;
    padding-bottom: 3px;
    border-bottom: 1.5px solid var(--rule);
    display: inline-block;
  }
  .person__title {
    font-size: 21px;
    font-weight: 400;
    margin-top: 3px;
  }
  .contact {
    position: absolute;
    left: 27px;
    top: 156px;
    list-style: none;
    color: var(--ink);
    font-size: 13.5px;
    line-height: 18px;
  }
  .contact__item {
    display: flex;
    align-items: flex-start;
    gap: 8px;
    margin-bottom: 2px;
  }
  .contact__icon {
    flex: 0 0 11px;
    width: 11px;
    height: 11px;
    margin-top: 3px;
  }
  .mark-dot {
    position: absolute;
    left: 355px;
    top: 126px;
    width: 44px;
    height: 44px;
    border-radius: 50%;
    background: var(--charcoal);
  }
</style>
</head>
<body>
<main class="stage">

  <section class="card card--front" aria-label="Card front">
    <svg class="card__shapes" viewBox="0 0 387 221" preserveAspectRatio="none" aria-hidden="true">
      <rect width="387" height="221" fill="var(--charcoal)"/>
      <ellipse cx="194" cy="110" rx="205" ry="140" transform="rotate(-18 194 110)" fill="var(--mid-grey)"/>
      <ellipse cx="190" cy="112" rx="180" ry="135" fill="var(--paper)"/>
    </svg>
    <div class="brand">
      <span class="brand__square" aria-hidden="true"></span>
      <span class="brand__name">HOLLERBY WHITLOCK GROUP</span>
    </div>
  </section>

  <section class="card card--back" aria-label="Card back">
    <svg class="card__shapes" viewBox="0 0 387 221" preserveAspectRatio="none" aria-hidden="true">
      <rect width="387" height="221" fill="var(--mid-grey)"/>
      <path d="M180 0 H387 V88 L335 128 Z" fill="var(--charcoal)"/>
      <path d="M0 0 H185 C290 18 368 80 348 120 C325 160 270 195 205 221 H0 Z" fill="var(--paper)"/>
    </svg>

    <span class="mark-dot" aria-hidden="true"></span>

    <div class="person">
      <h1 class="person__name">Daniel R. Whitlock</h1>
      <p class="person__title">co - founder &amp; partner</p>
    </div>

    <ul class="contact">
      <li class="contact__item">
        <svg class="contact__icon" viewBox="0 0 11 11" aria-hidden="true">
          <rect width="11" height="11" rx="2" fill="var(--charcoal)"/>
          <path d="M5.5 2 C3.8 2 3 3.2 3 4.3 C3 6 5.5 9 5.5 9 C5.5 9 8 6 8 4.3 C8 3.2 7.2 2 5.5 2 Z" fill="var(--paper)"/>
          <circle cx="5.5" cy="4.3" r="0.9" fill="var(--charcoal)"/>
        </svg>
        <span>418 Bramblewood Ave. SE<br>Suite 2716 Washington, D.C. 20019</span>
      </li>
      <li class="contact__item">
        <svg class="contact__icon" viewBox="0 0 11 11" aria-hidden="true">
          <rect width="11" height="11" rx="2" fill="var(--charcoal)"/>
          <path d="M3 2.5 L4.5 2.5 L5 4.3 L4.2 5 C4.6 5.9 5.1 6.4 6 6.8 L6.7 6 L8.5 6.5 L8.5 8 C5.5 8.3 2.7 5.5 3 2.5 Z" fill="var(--paper)"/>
        </svg>
        <span>(202) 555-0187</span>
      </li>
      <li class="contact__item">
        <svg class="contact__icon" viewBox="0 0 11 11" aria-hidden="true">
          <rect width="11" height="11" rx="2" fill="var(--charcoal)"/>
          <rect x="2.3" y="3.2" width="6.4" height="4.6" fill="none" stroke="var(--paper)" stroke-width="0.9"/>
          <path d="M2.3 3.2 L5.5 5.8 L8.7 3.2" fill="none" stroke="var(--paper)" stroke-width="0.9"/>
        </svg>
        <span>daniel@hollerbywhitlock.com</span>
      </li>
    </ul>
  </section>

</main>
</body>
</html>
```